Tobin's Jewelry Studio Needs a Moving Location Flyer

We need a flyer to inform our customers of our location moving. We will be moving to our city's downtown which is only 1 mile away from our current address. We will be having a moving sale ( Up to 80% off). The sale starts Sept. 8th Our business creates, sells, and repairs fine jewelry. Dimensions are 5"x8"

Target Market(s)

Women ages 25-55

Industry/Entity Type

Jewelry

Colors
85abd2
cfdeed

Requirements
Must have
• Our logo
• Mention of the sale
• Our current address
• 4785 Cresthaven Blvd.
• Dunmore, Ca 94318
• (415)826-3319
Nice to have
• Mention that we're relocating to downtown Dunmore (new location opening Nov. 1st.)

```html
<!DOCTYPE html>
<html lang="en">
<head>
<meta charset="utf-8">
<title>Tobin's Jewelry Studio – Moving Sale Flyer</title>
<link rel="stylesheet" href="https://fonts.googleapis.com/css2?family=Jost:wght@300;400;500&family=Playfair+Display:wght@400&display=swap">
<style>
  :root {
    --ink: #3b464b;
    --charcoal-dark: #141414;
    --charcoal-mid: #3a3a3a;
    --teal-light: #c4e7ec;
    --teal-soft: #a9dbe3;
    --teal-strong: #1ab3c9;
    --paper: #ffffff;
    --frame: #cfcfcf;
    --logo-ink: #2a2a2a;
  }
  * { margin: 0; padding: 0; box-sizing: border-box; }
  html, body { width: 800px; height: 1200px; overflow: hidden; background: var(--paper); }
  .flyer {
    position: relative; width: 800px; height: 1200px; overflow: hidden;
    font-family: "Jost", sans-serif; color: var(--ink);
  }
  .flyer__backdrop { position: absolute; inset: 0; }
  .hero-text { position: absolute; left: 87px; top: 0; width: 308px; color: var(--paper); }
  .hero-text__title {
    position: absolute; top: 74px; left: 0; width: 308px;
    font-weight: 300; font-size: 41px; letter-spacing: 2px; text-align: center; white-space: nowrap;
  }
  .hero-text__upto {
    position: absolute; top: 126px; left: 0; width: 308px;
    display: flex; align-items: center; gap: 8px; font-weight: 300; font-size: 21px;
  }
  .hero-text__upto::before, .hero-text__upto::after { content: ""; flex: 1; height: 2px; background: var(--paper); }
  .hero-text__figure {
    position: absolute; top: 116px; left: -8px;
    font-weight: 400; font-size: 212px; line-height: 1; letter-spacing: -6px;
  }
  .hero-text__off { position: absolute; top: 178px; left: 242px; font-weight: 300; font-size: 36px; }
  .hero-text__percent { position: absolute; top: 214px; left: 236px; font-weight: 300; font-size: 96px; line-height: 1; }
  .hero-text__rule { position: absolute; top: 342px; left: 0; width: 308px; height: 2px; background: var(--paper); }
  .hero-text__date {
    position: absolute; top: 356px; left: 0; width: 308px;
    font-weight: 400; font-size: 30px; letter-spacing: 4px; text-align: center; white-space: nowrap;
  }
  .announcement { position: absolute; left: 0; width: 800px; text-align: center; }
  .announcement__heading { top: 512px; font-weight: 500; font-size: 48px; letter-spacing: 5px; }
  .announcement__body { top: 568px; font-weight: 300; font-size: 23px; line-height: 33px; }
  .announcement__subheading { top: 680px; font-weight: 400; font-size: 31px; letter-spacing: 4px; }
  .announcement__address { top: 727px; font-weight: 300; font-size: 26px; }
  .announcement__phone { top: 771px; font-weight: 400; font-size: 37px; }
  .opening-badge {
    position: absolute; left: 274px; top: 836px; width: 251px; height: 46px;
    background: var(--teal-strong); color: var(--paper);
    font-weight: 300; font-size: 24px; line-height: 46px; text-align: center;
  }
  .services {
    position: absolute; left: 0; top: 925px; width: 800px; text-align: center;
    font-family: "Playfair Display", serif; font-size: 20px; letter-spacing: 7px; line-height: 33px; color: var(--ink);
  }
  .brand { position: absolute; left: 110px; top: 1075px; display: flex; align-items: center; gap: 14px; }
  .brand__mark { width: 64px; height: 64px; border-radius: 50%; background: var(--teal-light); }
  .brand__name { font-family: "Jost", sans-serif; font-weight: 500; font-size: 22px; color: var(--logo-ink); }
</style>
</head>
<body>
<main class="flyer">
  <svg class="flyer__backdrop" width="800" height="1200" viewBox="0 0 800 1200" aria-hidden="true">
    <defs>
      <linearGradient id="charcoal" x1="0" y1="0" x2="1" y2="1">
        <stop offset="0" stop-color="var(--charcoal-mid)"/>
        <stop offset="1" stop-color="var(--charcoal-dark)"/>
      </linearGradient>
      <linearGradient id="teal" x1="0" y1="0" x2="0" y2="1">
        <stop offset="0" stop-color="var(--teal-light)"/>
        <stop offset="1" stop-color="var(--teal-soft)"/>
      </linearGradient>
      <linearGradient id="pendant" x1="0" y1="0" x2="0" y2="1">
        <stop offset="0" stop-color="#8d8d93"/>
        <stop offset="0.5" stop-color="#6b4d86"/>
        <stop offset="1" stop-color="#4a2f63"/>
      </linearGradient>
      <linearGradient id="earrings" x1="0" y1="0" x2="1" y2="1">
        <stop offset="0" stop-color="#eeeeee"/>
        <stop offset="1" stop-color="#c9cbcd"/>
      </linearGradient>
    </defs>
    <rect class="hero-photo" x="0" y="0" width="800" height="520" fill="url(#charcoal)" role="img" aria-label="Photo of dark charcoal pieces"/>
    <rect class="hero-frame" x="35" y="33" width="725" height="500" fill="none" stroke="var(--frame)" stroke-width="4"/>
    <rect class="pendant-photo" x="470" y="0" width="170" height="410" rx="60" fill="url(#pendant)" opacity="0.85" role="img" aria-label="Photo of a silver pendant necklace with purple amethyst stones"/>
    <polygon class="panel-teal" points="0,477 800,379 800,1200 0,1200" fill="url(#teal)"/>
    <polygon class="panel-white" points="0,1015 800,1070 800,1200 0,1200" fill="var(--paper)"/>
    <rect class="earrings-photo" x="535" y="1010" width="205" height="176" rx="40" fill="url(#earrings)" role="img" aria-label="Photo of a pair of diamond flower drop earrings"/>
  </svg>

  <section class="hero-text">
    <h1 class="hero-text__title">MOVING SALE</h1>
    <div class="hero-text__upto">UP TO</div>
    <div class="hero-text__figure">80</div>
    <div class="hero-text__off">OFF</div>
    <div class="hero-text__percent">%</div>
    <div class="hero-text__rule"></div>
    <div class="hero-text__date">START SEPT. 8TH</div>
  </section>

  <h2 class="announcement announcement__heading">WE ARE MOVING</h2>
  <p class="announcement announcement__body">to our city's downtown which is only 1 mile away<br>from our current address.</p>
  <h3 class="announcement announcement__subheading">OUR NEW LOCATION</h3>
  <p class="announcement announcement__address">4785 Cresthaven Blvd. Dunmore, Ca 94318</p>
  <p class="announcement announcement__phone">(415)826-3319</p>
  <div class="opening-badge">Opening Nov. 1st</div>

  <p class="services">WE CREATES, SELLS<br>&amp; REPAIRS FINE JEWELRY</p>

  <div class="brand">
    <span class="brand__mark"></span>
    <span class="brand__name">tobin's jewelry studio</span>
  </div>
</main>
</body>
</html>
```